Hoofcare business card

I would like to create a business card design for my hoofcare business.

Front Side- would like to just include the logo and text as per the uploaded files- text font to match logo (upper and lower case).

Back side
- Include the details and contact information provided on the uploaded file.
- Also included on the back side- the uploaded TRIVN logo- keep it small on a top or bottom corner
- for rovendix and Plumtawyo contacts- please use the logos next to my usernames

```html
<!DOCTYPE html>
<html lang="en">
<head>
<meta charset="utf-8">
<title>KR Equine Hoofcare – Business Card</title>
<link href="https://fonts.googleapis.com/css2?family=Merriweather:wght@300;400&display=swap" rel="stylesheet">
<style>
  :root {
    --stage: #1b1b1b;
    --card: #262626;
    --card-edge: #1f1f1f;
    --ink: #f4f4f4;
    --ink-soft: #d9d9d9;
    --badge: #e9e9e9;
  }
  * { box-sizing: border-box; margin: 0; padding: 0; }
  html, body { width: 1200px; height: 988px; overflow: hidden; }
  body {
    background: var(--stage);
    font-family: "Merriweather", Georgia, serif;
    color: var(--ink);
    display: flex;
    flex-direction: column;
    align-items: center;
    justify-content: center;
    gap: 44px;
  }
  .card {
    position: relative;
    width: 760px;
    height: 434px;
    background: var(--card);
    border-radius: 26px;
    box-shadow: 0 3px 0 var(--card-edge), 0 14px 30px rgba(0,0,0,.55);
    overflow: hidden;
  }

  /* Front */
  .card-front {
    display: flex;
    flex-direction: column;
    align-items: center;
    text-align: center;
    padding-top: 110px;
  }
  .brand-lockup {
    display: flex;
    align-items: center;
    gap: 16px;
  }
  .brand-dot {
    width: 22px;
    height: 22px;
    border-radius: 50%;
    background: var(--ink);
    flex: none;
  }
  .brand-name {
    font-size: 40px;
    font-weight: 400;
    line-height: 1.2;
    color: var(--ink);
  }
  .front-tagline {
    margin-top: 70px;
    font-size: 21px;
    font-weight: 300;
    line-height: 1.45;
    color: var(--ink-soft);
  }

  /* Back */
  .card-back { padding: 0 56px; }
  .cert-badge {
    position: absolute;
    top: 30px;
    right: 40px;
    width: 74px;
    height: 74px;
    border-radius: 50%;
    background: var(--badge);
  }
  .role {
    margin-top: 120px;
    font-size: 25px;
    font-weight: 400;
  }
  .role-detail {
    margin-top: 8px;
    font-size: 15px;
    font-weight: 300;
    line-height: 1.45;
    color: var(--ink-soft);
  }
  .holder {
    margin-top: 44px;
    font-size: 31px;
    font-weight: 400;
  }
  .contact-list {
    margin-top: 14px;
    list-style: none;
    font-size: 16px;
    font-weight: 300;
    color: var(--ink-soft);
  }
  .contact-list li {
    display: flex;
    align-items: center;
    gap: 10px;
    height: 25px;
  }
  .contact-icon { width: 16px; height: 16px; flex: none; }
  .social-dot {
    width: 15px; height: 15px; flex: none;
    border-radius: 50%;
    background: var(--ink);
  }
</style>
</head>
<body>

  <section class="card card-front" aria-label="Card front">
    <div class="brand-lockup">
      <span class="brand-dot" aria-hidden="true"></span>
      <div class="brand-name">KR Equine Hoofcare</div>
    </div>
    <p class="front-tagline">Equine Barefoot Trimming and Rehabilitation<br>Wattle Bay and Surrounds</p>
  </section>

  <section class="card card-back" aria-label="Card back">
    <div class="cert-badge" role="img" aria-label="TRIVN certification badge"></div>

    <h2 class="role">Trivn Trained Barefoot Trimmer</h2>
    <p class="role-detail">Equine Barefoot Trimming and Rehabilitation<br>for all horses, ponies and donkeys</p>

    <h1 class="holder">Talia Renwick</h1>
    <ul class="contact-list">
      <li>
        <svg class="contact-icon" viewBox="0 0 16 16" aria-hidden="true">
          <rect x="4" y="1" width="8" height="14" rx="1.5" fill="none" stroke="#f4f4f4" stroke-width="1.3"/>
          <line x1="7" y1="12.5" x2="9" y2="12.5" stroke="#f4f4f4" stroke-width="1.3"/>
        </svg>
        0400518273
      </li>
      <li>
        <svg class="contact-icon" viewBox="0 0 16 16" aria-hidden="true">
          <rect x="1" y="3.5" width="14" height="9" fill="#f4f4f4"/>
          <polyline points="1,3.5 8,9 15,3.5" fill="none" stroke="#262626" stroke-width="1.3"/>
        </svg>
        krequinehoofcare@mailbox.com
      </li>
      <li><span class="social-dot" aria-hidden="true"></span>KR Equine Hoofcare</li>
      <li><span class="social-dot" aria-hidden="true"></span>krequinehoofcare</li>
    </ul>
  </section>

</body>
</html>
```